Chairside grafting for the dental nurse - start to finish

Book cover:

Book about dental implantology
Reader is a dental assistant
Introduction to surgical knowledge to case acceptance. We will start with the intro to implants that will cover population stats on tooth loss, how to make the patient trust the team, how to communicate with the patient. Then we will get more technical; bone loss, bone quality and quantity. We will also inform on pros and cons of different classic dental treatments vs implant treatment. Surgical knowledge deep into various aspects of implants procedures. An illustration of surgical instruments needed and motors and hand pieces. Operatory set up will be demonstrated. I’ll be guiding the role of the surgical assistant and non surgical assistant. At the end I’ll explain how to close an implant case. From single implants to more complex cases.

Target Market(s)

Dental assistants

Industry/Entity Type

Dental

Font styles to use
Other font styles liked:
• Mellifluous or addington

Colors
EE7325
F08F49
F5BC92
FAE3D3
FDF4ED

Requirements
Must have
• Dental implant, positive vibe, orange Colors, professional
Nice to have
• Sense of team spirit, uncluttered,
Should not have
• Images of people

```html
<!DOCTYPE html>
<html lang="en">
<head>
<meta charset="utf-8">
<title>Chairside Grafting for the Dental Nurse – Book Cover</title>
<link rel="stylesheet" href="https://fonts.googleapis.com/css2?family=Source+Serif+4:ital,opsz,wght@0,8..60,400;0,8..60,800;1,8..60,400;1,8..60,700&family=Kalam:wght@700&display=swap">
<style>
  :root {
    --page: #ffffff;
    --blush: #f9dcd3;
    --orange-light: #fb8446;
    --orange-deep: #f86a2c;
    --ribbon: #fb5f22;
    --ink-blue: #0a34e6;
    --white: #ffffff;
    --author: #fde6da;
  }
  * { margin: 0; padding: 0; box-sizing: border-box; }
  html, body {
    width: 1200px;
    height: 1000px;
    overflow: hidden;
    background: var(--page);
  }
  .cover {
    position: absolute;
    left: 375px;
    top: 201px;
    width: 418px;
    height: 591px;
    background: var(--blush);
    overflow: hidden;
  }
  .cover__field {
    position: absolute;
    inset: 0;
    width: 100%;
    height: 100%;
  }
  .title {
    position: absolute;
    left: 54px;
    top: 46px;
    font-family: "Source Serif 4", Georgia, serif;
    font-weight: 800;
    font-size: 47px;
    line-height: 40px;
    letter-spacing: -0.5px;
    color: var(--ink-blue);
  }
  .subtitle {
    position: absolute;
    left: 58px;
    top: 138px;
    font-family: "Source Serif 4", Georgia, serif;
    font-weight: 400;
    font-size: 18.5px;
    color: var(--ink-blue);
    white-space: nowrap;
  }
  .ribbon {
    position: absolute;
    left: 273px;
    top: 141px;
    width: 145px;
    height: 16px;
  }
  .ribbon__text {
    position: absolute;
    left: 288px;
    top: 140px;
    font-family: "Source Serif 4", Georgia, serif;
    font-style: italic;
    font-weight: 700;
    font-size: 13px;
    line-height: 18px;
    color: var(--white);
    white-space: nowrap;
  }
  .author {
    position: absolute;
    left: 60px;
    top: 170px;
    font-family: "Source Serif 4", Georgia, serif;
    font-style: italic;
    font-size: 12.5px;
    color: var(--author);
  }
  .tagline {
    position: absolute;
    font-family: "Kalam", "Comic Sans MS", cursive;
    font-weight: 700;
    font-size: 15px;
    line-height: 18px;
    color: var(--white);
    white-space: nowrap;
  }
  .tagline--top { left: 0; right: 0; top: 249px; text-align: center; }
  .tagline--left { left: 87px; top: 361px; }
  .tagline--right { left: 240px; top: 420px; }
  .tagline--bottom { left: 0; right: 0; top: 522px; text-align: center; }
  .implant-art {
    position: absolute;
    left: 164px;
    top: 277px;
    width: 89px;
    height: 231px;
  }
</style>
</head>
<body>
  <main class="cover">
    <svg class="cover__field" viewBox="0 0 418 591" aria-hidden="true">
      <defs>
        <linearGradient id="fieldGradient" x1="0" y1="0" x2="0" y2="1">
          <stop offset="0" stop-color="var(--orange-light)"/>
          <stop offset="1" stop-color="var(--orange-deep)"/>
        </linearGradient>
      </defs>
      <polygon points="0,170 201,170 207,183 418,183 418,591 0,591" fill="url(#fieldGradient)"/>
    </svg>

    <h1 class="title">Chairside<br>Grafting</h1>
    <p class="subtitle">For The Dental Nurse</p>

    <svg class="ribbon" viewBox="0 0 145 16" aria-hidden="true">
      <polygon points="7,0 145,0 145,16 0,16" fill="var(--ribbon)"/>
    </svg>
    <p class="ribbon__text">Start to Finish</p>

    <p class="author">author name</p>

    <p class="tagline tagline--top">The way to&nbsp; Efficiency</p>

    <svg class="implant-art" viewBox="0 0 89 231" role="img" aria-label="Illustration of a dental implant: white crown on a threaded titanium screw">
      <defs>
        <linearGradient id="implantTone" x1="0" y1="0" x2="0" y2="1">
          <stop offset="0" stop-color="#eef2ef"/>
          <stop offset="1" stop-color="#e3c4b2"/>
        </linearGradient>
      </defs>
      <rect x="0" y="0" width="89" height="231" rx="30" fill="url(#implantTone)" opacity="0.85"/>
    </svg>

    <p class="tagline tagline--left">What It Takes</p>
    <p class="tagline tagline--right">What Matters</p>
    <p class="tagline tagline--bottom">Benefiting The Entire TEAM</p>
  </main>
</body>
</html>
```